Meadowlark Learning Growth Partners (MLGP)

This is a professional business card. Logo and picture are a must on the front of the card. I am an educational consultant. I have been consulting for the past three years for a company. I am now opening my own company. My goal for my consulting company is to eventually consult all over America.

Target Market(s)

Educators, schools, professionals

Industry/Entity Type

Consulting

Contact Information for Business Card

Picture/logo on front, simple modern design

Font styles to use
Serif

Colors
85abd2
0355a3
3176b5
cedeed

Requirements
Must have
• picture, logo,
• Odessa Pruitt, Ed.S
• address 5073 Cormorant ridge Dr. Nashville, TN 37940
• Cell:616-555-0148
• Office: 629-555-0172
• www.Mlgpedu.example
• pruittodessa@mailbox.example

```html
<!DOCTYPE html>
<html lang="en">
<head>
<meta charset="utf-8">
<title>MLGP Business Card</title>
<link rel="stylesheet" href="https://fonts.googleapis.com/css2?family=Gilda+Display&family=Lexend:wght@500&display=swap">
<style>
  :root {
    --navy: #0a3f86;
    --brand-blue: #0355a3;
    --mid-blue: #3176b5;
    --sky: #85abd2;
    --pale: #cedeed;
    --page: #eef0f3;
    --serif: "Gilda Display", Georgia, serif;
    --sans: "Lexend", Arial, sans-serif;
  }
  * { margin: 0; padding: 0; box-sizing: border-box; }
  html, body { width: 1200px; height: 1200px; overflow: hidden; }
  body { background: var(--page); position: relative; }

  .card {
    position: absolute;
    left: 190px;
    width: 820px;
    height: 531px;
    overflow: hidden;
    box-shadow: 0 6px 18px rgba(0, 0, 0, 0.18);
  }

  /* Back of card */
  .card-back {
    top: 54px;
    background: radial-gradient(ellipse at 50% 45%, #d2e2f2 0%, #a9c4e2 45%, var(--sky) 100%);
    display: flex;
    align-items: center;
    justify-content: center;
    gap: 30px;
  }
  .card-back .mark-dot {
    width: 70px; height: 70px;
    border-radius: 50%;
    background: var(--navy);
  }
  .card-back .mark-name {
    font-family: var(--serif);
    font-size: 150px;
    color: var(--navy);
    letter-spacing: 6px;
    line-height: 1;
  }

  /* Front of card */
  .card-front {
    top: 615px;
    background: var(--pale);
  }
  .brand {
    position: absolute;
    left: 20px; top: 44px;
    display: flex;
    align-items: center;
  }
  .brand .mark-dot {
    width: 34px; height: 34px;
    border-radius: 50%;
    background: var(--navy);
    margin-right: 12px;
  }
  .brand .mark-name {
    font-family: var(--serif);
    font-size: 40px;
    color: var(--navy);
    letter-spacing: 2px;
  }
  .brand .divider {
    width: 2px; height: 100px;
    background: var(--navy);
    margin: 0 16px 0 14px;
  }
  .brand .company {
    font-family: var(--sans);
    font-weight: 500;
    font-size: 19px;
    line-height: 27px;
    color: var(--navy);
  }

  .contact {
    position: absolute;
    left: 20px; top: 224px;
    font-family: var(--serif);
    font-size: 25px;
    line-height: 37px;
    color: var(--navy);
    list-style: none;
  }

  .portrait {
    position: absolute;
    left: 438px; top: 20px;
    width: 382px; height: 511px;
    background: linear-gradient(180deg, var(--pale) 0%, #d9c7a4 30%, #e8c9b4 45%, #f2f2f0 65%, #1d2230 80%, #12151d 100%);
  }
</style>
</head>
<body>
  <section class="card card-back" aria-label="Card back">
    <span class="mark-dot"></span>
    <span class="mark-name">MLGP</span>
  </section>

  <section class="card card-front" aria-label="Card front">
    <div class="brand">
      <span class="mark-dot"></span>
      <span class="mark-name">MLGP</span>
      <span class="divider"></span>
      <div class="company">Meadowlark<br>Learning<br>Growth<br>Partners</div>
    </div>

    <ul class="contact">
      <li>Odessa Pruitt, Ed.S</li>
      <li>address 5073 Cormorant ridge</li>
      <li>Dr. Nashville, TN 37940</li>
      <li>Cell:616-555-0148</li>
      <li>Office: 629-555-0172</li>
      <li>www.Mlgpedu.example</li>
      <li>pruittodessa@mailbox.example</li>
    </ul>

    <div class="portrait" role="img" aria-label="Portrait photo of the consultant in a dark blazer and white blouse"></div>
  </section>
</body>
</html>
```